Birch Spire Kilo Marsh website

we need a website to cater to 2 aspect of the business. We have Birch spire residence and birch spire office. For the office, we will get their inquire and arrange a face to face meetup to show them the office area for rent. For the residence side, it will need to be like stayrio or velupa.com. we want to allow them to book online for the date they need. We have a total of 10 different room configurations starting at $70 per night and up depending on the size of the room. example of the design is https://lumbrahaven.com/

Target Market(s)

the website should have detail information on the layout, designs, and luxury of the building.

Industry/Entity Type

office and service appartment rental/lease

Coding

Coded - Design and coding required

Number of Pages Required

5+ page

Requirements
Must have
• a luxury perspective
Nice to have
• example https://lumbrahaven.com/

```html
<!DOCTYPE html>
<html lang="en">
<head>
<meta charset="utf-8">
<title>Birch Spire Kilo Marsh</title>
<link href="https://fonts.googleapis.com/css2?family=Roboto:wght@300;400;500;700&display=swap" rel="stylesheet">
<style>
:root{
  --black:#000;
  --gold:#d69b2b;
  --gold-btn:#d9a13b;
  --gold-soft:#e9cd96;
  --ink:#1e1e1e;
  --muted:#5d5d5d;
  --line:#cfcfcf;
  --panel:#ffffff;
  --cream:#faf6f1;
  --star:#f07d12;
}
*{box-sizing:border-box;margin:0;padding:0}
html,body{width:1200px;height:3307px;overflow:hidden}
body{position:relative;background:#fff;font-family:"Roboto",sans-serif;color:var(--ink)}
.abs{position:absolute}
.header{left:0;top:0;width:1200px;height:70px;background:var(--black)}
.brand{left:112px;top:24px;color:var(--gold);font-size:17px;font-weight:500;letter-spacing:.5px}
.btn-outline{left:747px;top:19px;width:90px;height:34px;border:1.5px solid var(--gold);color:#fff;font-size:13px;display:flex;align-items:center;justify-content:center;border-radius:2px}
.btn-gold{left:851px;top:19px;width:134px;height:34px;background:var(--gold-btn);color:#1a1a1a;font-size:13px;display:flex;align-items:center;justify-content:center;border-radius:2px}
.icon-cart{left:1012px;top:26px}
.icon-menu{left:1063px;top:26px}
.hero{left:0;top:70px;width:1200px;height:410px;background:linear-gradient(180deg,#6d94bc 0%,#9db6cc 35%,#7f8a8e 62%,#6c6a4a 85%,#544d2a 100%)}
.hero-text{left:0;width:1200px;text-align:center;color:#fff;text-shadow:0 2px 6px rgba(0,0,0,.35)}
.hero-kicker{top:184px;font-size:33px;font-weight:700}
.hero-title{top:224px;font-size:50px;font-weight:700}
.hero-sub{top:288px;font-size:19px;font-weight:400}
.search-card{left:112px;top:373px;width:977px;height:143px;background:#fff;border-radius:4px;box-shadow:0 4px 14px rgba(80,110,170,.25)}
.tab{top:348px;height:50px;display:flex;align-items:center;justify-content:center;font-size:17px;font-weight:500;text-transform:uppercase}
.tab-res{left:136px;width:249px;background:#fff;color:var(--gold);box-shadow:0 2px 8px rgba(0,0,0,.15)}
.tab-off{left:400px;width:224px;background:var(--gold-btn);color:#1a1a1a}
.stay{top:422px;font-size:17px;color:#333}
.field{top:461px;height:38px;border:1px solid var(--line);font-size:15px;color:#888;padding:0 9px;display:flex;align-items:center;justify-content:space-between}
.search-btn{left:950px;top:461px;width:125px;height:38px;background:var(--gold-btn);color:#fff;font-weight:700;font-size:17px;display:flex;align-items:center;justify-content:center;border-radius:3px}
.photo{border-radius:1px}
.feature-panel{background:#fff;padding:18px 24px}
.feature-panel h3{font-size:25px;font-weight:500;margin-bottom:14px}
.feature-panel p{font-size:14.5px;line-height:21px;color:var(--muted);font-weight:300}
.feature-link{margin-top:22px;font-size:14.5px;font-weight:500;display:flex;align-items:center;gap:12px}
.gold{color:var(--gold)}
.shadow{box-shadow:0 2px 10px rgba(0,0,0,.10)}
.section-title{left:110px;font-size:25px;font-weight:500}
.section-sub{left:110px;font-size:15px}
.room-panel{background:#fff;padding:22px 19px 0}
.room-panel h4{font-size:17px;font-weight:400;margin-bottom:12px}
.meta{font-size:14px;color:#666;margin-bottom:10px;white-space:nowrap}
.meta i{font-style:normal;margin:0 10px;color:#888}
.price{font-size:17px;font-weight:500}
.price span{font-size:13px;font-weight:400}
.more{margin-top:30px;font-size:14.5px;font-weight:500;display:flex;align-items:center;gap:14px}
.arrow-btn{width:30px;height:30px;border-radius:50%;background:#fff;display:flex;align-items:center;justify-content:center;font-size:18px}
.testi{padding:24px 33px 24px 17px;background:var(--cream)}
.testi.hl{background:var(--gold-soft);box-shadow:0 2px 8px rgba(0,0,0,.12)}
.testi h5{font-size:20px;font-weight:400;margin-bottom:10px}
.testi p{font-size:14.5px;line-height:22px;color:#555;font-weight:300}
.stars{margin-top:14px;color:var(--star);font-size:19px;letter-spacing:4px}
.skyline{left:0;top:2540px;width:1200px;height:192px;background:linear-gradient(180deg,#fff 0%,#eef3f7 55%,#e8eef4 100%)}
.foot-col h6{font-size:15.5px;font-weight:400;margin-bottom:8px}
.foot-col li{list-style:none;font-size:12.5px;line-height:20.5px;color:#333}
.footer{left:0;top:3006px;width:1200px;height:301px;background:var(--black)}
.foot-mark{left:565px;top:3047px;width:70px;height:80px;border:2px solid var(--gold)}
.foot-name{left:0;width:1200px;top:3138px;text-align:center;color:var(--gold);font-size:27px;font-weight:400;letter-spacing:1px}
.foot-links{left:0;width:1200px;top:3182px;text-align:center;color:#aaa;font-size:15px}
.foot-copy{left:0;width:1200px;top:3210px;text-align:center;color:#aaa;font-size:14px}
.social{left:0;width:1200px;top:3252px;text-align:center;color:var(--gold);font-size:14px;letter-spacing:1px}
</style>
</head>
<body>
<header class="abs header"></header>
<div class="abs brand">Birch Spire Kilo Marsh</div>
<div class="abs btn-outline">Sign In</div>
<div class="abs btn-gold">Create Account</div>
<svg class="abs icon-cart" width="18" height="16" viewBox="0 0 18 16"><path d="M1 2h3l2 8h8l2-6H5" fill="none" stroke="#fff" stroke-width="1.6"/><circle cx="7" cy="13.5" r="1.5" fill="#fff"/><circle cx="13" cy="13.5" r="1.5" fill="#fff"/></svg>
<svg class="abs icon-menu" width="26" height="18" viewBox="0 0 26 18"><path d="M0 1h26M0 9h26M0 17h26" stroke="#fff" stroke-width="1.4"/></svg>

<div class="abs hero" role="img" aria-label="City skyline of tall office towers under a blue sky with trees below"></div>
<div class="abs hero-text hero-kicker">Birch Spire Kilo Marsh</div>
<div class="abs hero-text hero-title">Find your next stay</div>
<div class="abs hero-text hero-sub">Find the rental assets you need, or earn money leading yours</div>

<div class="abs search-card"></div>
<div class="abs tab tab-res">Birch Spire Residence</div>
<div class="abs tab tab-off">Birch Spire Office</div>
<div class="abs stay" style="left:140px">Overnight Stays</div>
<div class="abs stay" style="left:313px">Day Use Stays</div>
<div class="abs field" style="left:124px;width:264px">Enter a destination or property
  <svg width="14" height="14" viewBox="0 0 14 14"><circle cx="6" cy="6" r="4.5" fill="none" stroke="#bbb" stroke-width="1.4"/><path d="M9.5 9.5l3.5 3.5" stroke="#bbb" stroke-width="1.4"/></svg></div>
<div class="abs field" style="left:403px;width:262px">Check in
  <svg width="14" height="14" viewBox="0 0 14 14"><rect x="1" y="2" width="12" height="11" fill="none" stroke="#bbb"/><path d="M1 5h12M4 8h2M8 8h2M4 10.5h2M8 10.5h2" stroke="#bbb"/></svg></div>
<div class="abs field" style="left:680px;width:263px">Check Out
  <svg width="14" height="14" viewBox="0 0 14 14"><rect x="1" y="2" width="12" height="11" fill="none" stroke="#bbb"/><path d="M1 5h12M4 8h2M8 8h2M4 10.5h2M8 10.5h2" stroke="#bbb"/></svg></div>
<div class="abs search-btn">Search</div>

<div class="abs photo" style="left:112px;top:556px;width:472px;height:333px;background:linear-gradient(180deg,#e8edf2,#d9dcd8 60%,#9aa58a)" role="img" aria-label="White modern apartment building with balconies and greenery"></div>
<div class="abs photo" style="left:616px;top:556px;width:472px;height:333px;background:linear-gradient(160deg,#3d78c6,#7fb0e6 45%,#c9d9ea 70%,#3b5f8f)" role="img" aria-label="Glass office towers seen from below against a blue sky"></div>
<div class="abs feature-panel" style="left:174px;top:856px;width:410px;height:174px">
  <h3>Find Better Places to Stay.</h3>
  <p>Lorem ipsum is placeholder text commonly used in the graphic, print, and publishing industries for previewing layouts and visual mockups.</p>
  <div class="feature-link">View More Birch Spire Residence <svg width="24" height="10" viewBox="0 0 24 10"><path d="M0 5h22M17 1l5 4-5 4" fill="none" stroke="#1e1e1e" stroke-width="1.5"/></svg></div>
</div>
<div class="abs feature-panel shadow" style="left:678px;top:856px;width:410px;height:174px">
  <h3 class="gold">Find Better Places to Work.</h3>
  <p>Lorem ipsum is placeholder text commonly used in the graphic, print, and publishing industries for previewing layouts and visual mockups.</p>
  <div class="feature-link gold">View More Birch Spire Office <svg width="24" height="10" viewBox="0 0 24 10"><path d="M0 5h22M17 1l5 4-5 4" fill="none" stroke="#d69b2b" stroke-width="1.5"/></svg></div>
</div>

<div class="abs section-title" style="top:1122px">Handpicked Our Residential Projects</div>
<div class="abs section-sub" style="top:1160px">Lorem ipsum is placeholder text commonly used.</div>

<div class="abs photo" style="left:47px;top:1210px;width:356px;height:267px;background:linear-gradient(180deg,#8fa2b4,#b7aa95 55%,#5e5347)" role="img" aria-label="Bedroom with large windows overlooking mountains"></div>
<div class="abs photo" style="left:422px;top:1210px;width:356px;height:267px;background:linear-gradient(180deg,#dcd5ca,#c9bba5 60%,#8f7558)" role="img" aria-label="Bright living room with sofa, coffee table and plant"></div>
<div class="abs photo" style="left:797px;top:1210px;width:355px;height:267px;background:linear-gradient(180deg,#e9e8e6,#bdb8b2 60%,#8f8a87)" role="img" aria-label="Grey bedroom with ceiling fan and windows"></div>
<div class="abs arrow-btn" style="left:112px;top:1344px">&lsaquo;</div>
<div class="abs arrow-btn" style="left:1057px;top:1344px">&rsaquo;</div>

<div class="abs room-panel" style="left:64px;top:1445px;width:312px;height:176px">
  <h4>One Bed Room</h4><div class="meta">Size: 47<i>|</i>Floor: 12<i>|</i>Room No: F1201b</div>
  <div class="price">$70 <span>per night</span></div>
  <div class="more">View More <svg width="24" height="10" viewBox="0 0 24 10"><path d="M0 5h22M17 1l5 4-5 4" fill="none" stroke="#1e1e1e" stroke-width="1.5"/></svg></div></div>
<div class="abs room-panel shadow" style="left:439px;top:1445px;width:313px;height:176px">
  <h4 class="gold">Two Bed Room</h4><div class="meta">Size: 47<i>|</i>Floor: 12<i>|</i>Room No: F1201b</div>
  <div class="price">$70 <span>per night</span></div>
  <div class="more gold">View More <svg width="24" height="10" viewBox="0 0 24 10"><path d="M0 5h22M17 1l5 4-5 4" fill="none" stroke="#d69b2b" stroke-width="1.5"/></svg></div></div>
<div class="abs room-panel" style="left:813px;top:1445px;width:313px;height:176px">
  <h4>One Bed Room</h4><div class="meta">Size: 47<i>|</i>Floor: 12<i>|</i>Room No: F1201b</div>
  <div class="price">$70 <span>per night</span></div>
  <div class="more">View More <svg width="24" height="10" viewBox="0 0 24 10"><path d="M0 5h22M17 1l5 4-5 4" fill="none" stroke="#1e1e1e" stroke-width="1.5"/></svg></div></div>

<div class="abs section-title" style="top:1692px">Handpicked Our Office Projects</div>
<div class="abs section-sub" style="top:1731px">Lorem ipsum is placeholder text commonly used.</div>

<div class="abs photo" style="left:47px;top:1780px;width:356px;height:268px;background:linear-gradient(120deg,#3a3d42,#9fb2c2 50%,#e0e6ea)" role="img" aria-label="Open office with desks, chairs and floor-to-ceiling windows"></div>
<div class="abs photo" style="left:422px;top:1780px;width:356px;height:268px;background:linear-gradient(180deg,#f0e6d6,#c7a57d 55%,#7b5436)" role="img" aria-label="Office lounge with pendant lamps, wood wall and seating"></div>
<div class="abs photo" style="left:797px;top:1780px;width:355px;height:268px;background:linear-gradient(180deg,#f1f1f0,#d7d5d2 55%,#6d7379)" role="img" aria-label="Office workstations with computer monitors and plants"></div>
<div class="abs arrow-btn" style="left:112px;top:1915px">&lsaquo;</div>
<div class="abs arrow-btn" style="left:1057px;top:1915px">&rsaquo;</div>

<div class="abs room-panel" style="left:64px;top:2016px;width:312px;height:176px">
  <h4>Type A Studio</h4><div class="meta">Size: 47<i>|</i>Floor: 12<i>|</i>Room No: F1201b</div>
  <div class="price">$2500 <span>per month</span></div>
  <div class="more">View More <svg width="24" height="10" viewBox="0 0 24 10"><path d="M0 5h22M17 1l5 4-5 4" fill="none" stroke="#1e1e1e" stroke-width="1.5"/></svg></div></div>
<div class="abs room-panel shadow" style="left:439px;top:2016px;width:313px;height:176px">
  <h4 class="gold">Type B Studio</h4><div class="meta">Size: 47<i>|</i>Floor: 12<i>|</i>Room No: F1201b</div>
  <div class="price gold">$2500 <span>per month</span></div>
  <div class="more gold">View More <svg width="24" height="10" viewBox="0 0 24 10"><path d="M0 5h22M17 1l5 4-5 4" fill="none" stroke="#d69b2b" stroke-width="1.5"/></svg></div></div>
<div class="abs room-panel" style="left:813px;top:2016px;width:313px;height:176px">
  <h4>Type D Studio</h4><div class="meta">Size: 47<i>|</i>Floor: 12<i>|</i>Room No: F1201b</div>
  <div class="price">$2500 <span>per month</span></div>
  <div class="more">View More <svg width="24" height="10" viewBox="0 0 24 10"><path d="M0 5h22M17 1l5 4-5 4" fill="none" stroke="#1e1e1e" stroke-width="1.5"/></svg></div></div>

<div class="abs skyline" role="img" aria-label="Faint hazy city skyline backdrop"></div>
<div class="abs section-title" style="top:2304px">What our customers are saying about Birch Spire Kilo Marsh</div>

<div class="abs testi" style="left:110px;top:2370px;width:312px;height:200px">
  <h5>Mirela T. Vance</h5><p>Lorem ipsum is placeholder text commonly used in the graphic, print, and publishing industries for previewing layouts and visual mockups.</p><div class="stars">★★★★★</div></div>
<div class="abs testi hl" style="left:442px;top:2370px;width:313px;height:200px">
  <h5>Mirela T. Vance</h5><p>Lorem ipsum is placeholder text commonly used in the graphic, print, and publishing industries for previewing layouts and visual mockups.</p><div class="stars">★★★★★</div></div>
<div class="abs testi" style="left:775px;top:2370px;width:312px;height:200px">
  <h5>Mirela T. Vance</h5><p>Lorem ipsum is placeholder text commonly used in the graphic, print, and publishing industries for previewing layouts and visual mockups.</p><div class="stars">★★★★★</div></div>
<div class="abs more" style="left:110px;top:2600px;margin:0">View All Testimonials <svg width="24" height="10" viewBox="0 0 24 10"><path d="M0 5h22M17 1l5 4-5 4" fill="none" stroke="#1e1e1e" stroke-width="1.5"/></svg></div>

<div class="abs foot-col" style="left:113px;top:2790px"><h6>Help</h6><ul><li>Help center</li><li>FAQs</li><li>Privacy policy</li><li>Cookie policy</li><li>Terms of use</li><li>Manage cookie settings</li><li>Digital Services Act (EU)</li></ul></div>
<div class="abs foot-col" style="left:438px;top:2790px"><h6>Company</h6><ul><li>About us</li><li>Careers</li><li>Press</li><li>Blog</li></ul></div>
<div class="abs foot-col" style="left:690px;top:2790px"><h6>Destinations</h6><ul><li>Help center</li><li>FAQs</li><li>Privacy policy</li><li>Cookie policy</li><li>Terms of use</li><li>Manage cookie settings</li><li>Digital Services Act (EU)</li></ul></div>
<div class="abs foot-col" style="left:1010px;top:2790px"><h6>Get the app</h6><ul><li>Orchard app</li><li>Verdant app</li></ul></div>

<footer class="abs footer"></footer>
<div class="abs foot-mark"></div>
<div class="abs foot-name">Birch Spire Kilo Marsh</div>
<div class="abs foot-links">Privacy Policy &nbsp; | &nbsp; Terms and Conditions &nbsp; | &nbsp; Customer Service</div>
<div class="abs foot-copy">Copyright © 2024. Birch Spire Kilo Marsh.</div>
<div class="abs social">Folio &nbsp; Chirp &nbsp; Linkr &nbsp; Snapr</div>
</body>
</html>
```